Guaranteed Job - Sleek Sexy Business Card UV Spot

Im looking for a sleek and sexy business card, that resembles elite or VIP status status.
our business is corinvale.example
you can view our products on there, but our main audience for handing out our cards will be for people in the hospitality industry, so it will need to impress high management and CEO of hotels and restaurants, bars, clubs etc...
the card features will have UV spot on both sides, 400gsm stock. standard size.
Artwork should be 86 x 54mm + 2mm bleed = 90 x 58mm
it should have a nice "unique" uv spot pattern that highlights the card, not a repeated pattern, theres no originality there, and it will be disregarded.
The written material will be:
Corin Vale Hospitality College (logo)
Tobin Marsh
Director
Phone: 1300 615 737
Mobile: 0455 817 296
Email: info@corinvale.example
website: www.corinvale.example
I'm looking for originality here, i don't want just a simple stock card, want something that has a wow factor for people.
You will find the logo attached. you may invert the white to black words to suit the background as you please.
thank you and good luck
As a side note, ive received a lot of proposals, im too busy to give feedback to each and every one, so if i havent provided feedback for your design within 24 hours, then consider it not acceptable, and you could resubmit another design.
So far i have not seen any design that stood out for me, they all seem pretty generic. there nothing thats unique, i would figure for the amount that im offering, that people would put some more effort and creativity into the design.
so far over 200 designs submitted, and nothing i have seen looks very original, everything looks like a different variation of the same stuff, i said it very clearly i wanted something unique, the only thing that has come close to it so far is this one
Reason: Ive received alot of design concepts and i have reviewed everyone, but i havent had time to give feedback to every single one, only the ones that have interested me, if i havent responded, its because i havent found it good enough.
so far only a few design have been on par with what ive been looking for, an attractive eye popping design.
heres a few of them,
http://files.pixelbazaar.example/design_img/51736/62418/62418_2840915_51736_image.jpg
http://files.pixelbazaar.example/design_img/51736/68254/68254_2841377_51736_image.jpg
theyre, both unique and original, and eye catching, the only thing theyre missing is the sexyness.
if you still think you have some creativity left in your minds, then throw it on here.
Reason: Sorry guys for the delay, I was in a serious accident and out of commission for the past few months, I'm just slowly recovering now, please bare with me as i try to attend to this project, it may take me awhile as I have other projects that are on standby, I'm not 100% at the moment, so im extending the deadline for 2 weeks right now. Thanks for your patience.
Hospitality

```html
<!DOCTYPE html>
<html lang="en">
<head>
<meta charset="utf-8">
<title>Corin Vale Hospitality College – Business Card</title>
<link rel="stylesheet" href="https://fonts.googleapis.com/css2?family=Oswald:wght@400;500&family=Roboto+Condensed:wght@400;700&display=swap">
<style>
  :root {
    --bg: #e7e2d8;
    --card-top: #1f1f1f;
    --card-bottom: #121212;
    --white: #f4f4f4;
    --soft-white: #cfcfcf;
    --blue: #5ab4dc;
    --rule: #8a8a8a;
    --tab-top: #b9b9b9;
    --tab-bottom: #8d8d8d;
    --tab-text: #3a3a3a;
  }
  * { margin: 0; padding: 0; box-sizing: border-box; }
  html, body { width: 1200px; height: 902px; overflow: hidden; }
  body {
    background: var(--bg);
    font-family: "Roboto Condensed", "Arial Narrow", sans-serif;
    position: relative;
  }
  .card {
    position: absolute;
    top: 281px;
    width: 540px;
    height: 340px;
    border-radius: 24px;
    background: linear-gradient(160deg, var(--card-top), var(--card-bottom));
    overflow: hidden;
  }
  .card--front { left: 40px; }
  .card--back { left: 620px; }

  /* Front */
  .brand {
    position: absolute;
    display: flex;
    align-items: center;
    gap: 22px;
  }
  .card--front .brand { left: 52px; bottom: 58px; }
  .brand__square {
    width: 70px; height: 70px;
    background: var(--blue);
    flex: none;
  }
  .brand__name {
    font-family: "Oswald", "Arial Narrow", sans-serif;
    font-weight: 500;
    color: var(--white);
    text-transform: uppercase;
    line-height: 0.98;
  }
  .card--front .brand__name { font-size: 46px; }
  .brand__name span { display: block; }
  .brand__name .brand__sub { font-size: 0.44em; letter-spacing: 0.09em; margin-top: 6px; }

  /* Back */
  .card--back .brand { left: 34px; bottom: 44px; gap: 12px; }
  .card--back .brand__square { width: 34px; height: 34px; }
  .card--back .brand__name { font-size: 23px; }

  .divider {
    position: absolute;
    left: 236px; top: 150px;
    width: 1px; height: 150px;
    background: var(--soft-white);
  }
  .contact {
    position: absolute;
    right: 34px; top: 30px;
    width: 232px;
    text-align: right;
    color: var(--white);
  }
  .contact__name { font-size: 27px; font-weight: 700; line-height: 1; }
  .contact__first { color: var(--blue); }
  .contact__role { font-size: 15px; margin-top: 3px; }
  .contact__list { list-style: none; margin-top: 10px; }
  .contact__item {
    display: flex;
    justify-content: flex-end;
    align-items: center;
    gap: 10px;
    font-size: 15px;
    padding: 9px 0;
    border-top: 1px dashed var(--rule);
  }
  .contact__item:last-child { border-bottom: 1px dashed var(--rule); }
  .contact__icon { width: 14px; height: 14px; flex: none; }

  .web-tab {
    position: absolute;
    right: 0; bottom: 0;
    width: 210px; height: 40px;
    border-top-left-radius: 14px;
    background: linear-gradient(180deg, var(--tab-top), var(--tab-bottom));
    color: var(--tab-text);
    font-size: 14px;
    letter-spacing: 0.04em;
    display: flex; align-items: center; justify-content: center;
  }
</style>
</head>
<body>

<section class="card card--front" aria-label="Card front">
  <div class="brand">
    <div class="brand__square"></div>
    <p class="brand__name"><span>Corin</span><span>Vale</span><span class="brand__sub">Hospitality College</span></p>
  </div>
</section>

<section class="card card--back" aria-label="Card back">
  <div class="brand">
    <div class="brand__square"></div>
    <p class="brand__name"><span>Corin</span><span>Vale</span><span class="brand__sub">Hospitality College</span></p>
  </div>

  <div class="divider"></div>

  <div class="contact">
    <p class="contact__name"><span class="contact__first">Tobin</span> Marsh</p>
    <p class="contact__role">Director</p>
    <ul class="contact__list">
      <li class="contact__item">1300 615 737
        <svg class="contact__icon" viewBox="0 0 14 14" aria-hidden="true"><path fill="#5ab4dc" d="M1 4c0-2 1.5-3 6-3s6 1 6 3v1H10V3.5H4V5H1z M3 6h8l1.5 7h-11z"/></svg>
      </li>
      <li class="contact__item">0455 817 296
        <svg class="contact__icon" viewBox="0 0 14 14" aria-hidden="true"><rect x="3.5" y="0.5" width="7" height="13" rx="1.2" fill="#5ab4dc"/><rect x="5" y="2" width="4" height="8" fill="#121212"/></svg>
      </li>
      <li class="contact__item">info@corinvale.example
        <svg class="contact__icon" viewBox="0 0 14 14" aria-hidden="true"><rect x="0.5" y="2.5" width="13" height="9" fill="#5ab4dc"/><path d="M0.5 2.5L7 8l6.5-5.5" fill="none" stroke="#121212" stroke-width="1.2"/></svg>
      </li>
    </ul>
  </div>

  <div class="web-tab">www.corinvale.example</div>
</section>

</body>
</html>
```